Quorvix Letter head

Quorvix is a young and energetic software development consultancy. We spend our time working with clients to turn what ever is in their heads in to software.
We are trying to create an image of a high class software boutique who build class leading bespoke solutions.
We need a sharp letter head that looks great on high quality media.
We like bold colours and distinctive design. So show us what you can do.
Industry/Entity Type
Software
Requirements
Must have
- Our company is based in the UK and are requried to have on the paper somewhere the following information:
* Registered company name: Quorvix Ltd
* Registered company number
* VAT registration number
In addition we also want the following:
* An email address
* Telephone number
* Website address
An example of what some pages have in their footer is something like the following:
Quorvix Ltd is registered in England and Wales. Reg. no: 5316274
Registered office: 48 Cobblewick Road, Harlow Essex, CM93TP. Tel: 07712365081
You do not have to use this sentance but please make sure your design incorporates accommodates the requirements for UK based companies

```html
<!DOCTYPE html>
<html lang="en">
<head>
<meta charset="utf-8">
<title>Quorvix Letterhead</title>
<link rel="stylesheet" href="https://fonts.googleapis.com/css2?family=Questrial&display=swap">
<style>
  :root {
    --backdrop: #e9e6e1;
    --paper: #ffffff;
    --brand-red: #b81c2c;
    --brand-red-deep: #93141f;
    --ink: #1e1e1e;
    --ink-soft: #555555;
    --ghost: #ececec;
    --ghost-red: #a81826;
  }
  * { margin: 0; padding: 0; box-sizing: border-box; }
  html, body { width: 1200px; height: 720px; overflow: hidden; }
  body {
    background: var(--backdrop);
    font-family: "Questrial", "Century Gothic", sans-serif;
    color: var(--ink);
    position: relative;
  }
  .sheet {
    position: absolute;
    top: 40px;
    width: 452px;
    height: 640px;
    box-shadow: 0 6px 18px rgba(0,0,0,0.18);
    overflow: hidden;
  }
  .letter-front { left: 130px; background: var(--paper); }
  .letter-back {
    left: 618px;
    background: linear-gradient(160deg, var(--brand-red-deep) 0%, var(--brand-red) 55%, var(--brand-red-deep) 100%);
  }
  .brand-name {
    position: absolute;
    top: 30px;
    left: 0; right: 0;
    text-align: center;
    font-size: 24px;
    letter-spacing: 1px;
    color: var(--brand-red);
  }
  .recipient {
    position: absolute;
    top: 100px;
    left: 78px;
    font-size: 8.5px;
    line-height: 11px;
    font-style: italic;
  }
  .recipient strong { font-weight: 700; }
  .letter-body {
    position: absolute;
    top: 178px;
    left: 58px;
    width: 340px;
    font-size: 8.5px;
    line-height: 11.5px;
  }
  .letter-body p { margin-bottom: 10px; }
  .signature {
    position: absolute;
    top: 400px;
    left: 58px;
    font-size: 8.5px;
    line-height: 11px;
  }
  .signature strong { font-weight: 700; }
  .ghost-name {
    position: absolute;
    top: 508px;
    left: 0; right: 0;
    text-align: center;
    font-size: 58px;
    letter-spacing: 2px;
    color: var(--ghost);
  }
  .footer-contact {
    position: absolute;
    bottom: 30px;
    left: 0; right: 0;
    text-align: center;
    font-size: 6.5px;
    color: var(--ink-soft);
    line-height: 11px;
  }
  .footer-contact strong { color: var(--ink); font-weight: 700; }
  .footer-contact .divider { color: var(--brand-red); padding: 0 3px; }
  .back-ghost-name {
    position: absolute;
    top: 470px;
    left: 50px;
    font-size: 56px;
    letter-spacing: 2px;
    color: var(--ghost-red);
  }
  .back-web {
    position: absolute;
    top: 552px;
    left: 118px;
    font-size: 9px;
    color: #ffffff;
  }
  .back-web strong { font-weight: 700; }
</style>
</head>
<body>
  <section class="sheet letter-front">
    <div class="brand-name">QUORVIX</div>

    <address class="recipient">
      <strong>Mr. Daniel Hart</strong><br>
      Managing Director<br>
      Northfield Capital<br>
      220 West Oak Avenue<br>
      USA
    </address>

    <div class="letter-body">
      <p>Lorem Ipsum is simply dummy text for printing and typesetting industry. Lorem Ipsum has been the industry's standard dummy text since the 1500s, when an unknown printer galley of type and scrambled it to make a type specimen book. It has survived not only manual but also the leap into electronic typesetting, remaining essentially un changed. It was popularised in the 1960s with the release of Typeline sheets containing Lorem Ipsum pass and more recently with desktop publishing software like Linden PageSet including versions of Lorem Ipsum.</p>
      <p>Country to popular belief, Lorem Ipsum is not simply random text. It has roots in a piece of sical Latin literature from 45 BC, making it over 2000 years old. Thomas Ellery, a prfessor at Ashworth College in Virginia, found the undoubtable sorce. Lorem Ipsum comes from section 1.10.32 and 1.10.33 of "de Finibus Bonorum et Molorum" (The Extremes of Good and Evil) by Marcus Vell, written in 45 BC. This book is a treatise on the theory of ethics, very popular during Renassiance.</p>
      <p>Thank you for being one of our valued customers.</p>
    </div>

    <div class="signature">
      <strong>Name Here</strong><br>
      CEO
    </div>

    <div class="ghost-name" aria-hidden="true">QUORVIX</div>

    <footer class="footer-contact">
      <strong>Quorvix Ltd.</strong> 48 Cobblewick Road, Harlow Essex, CM93TP
      <span class="divider">|</span>07712365081
      <span class="divider">|</span>01279 440 218
      <span class="divider">|</span>info@quorvix.co.uk<br>
      Reg. No. 5316274 Registered in England <span class="divider">|</span> VAT Reg No.: GB 418 2290 37
    </footer>
  </section>

  <section class="sheet letter-back">
    <div class="back-ghost-name" aria-hidden="true">QUORVIX</div>
    <div class="back-web"><strong>www.quorvix</strong>.co.uk</div>
  </section>
</body>
</html>
```